A parent Company needs a website as a leading diversified business in industrial Conglomerates in Af

Tesku Group is a private (Holding) limited liability company incorporated under the Companies Code, 1963 (Act 179) in November, 2013 to following the speedy growth in numbers of its current subsidiaries which has been founded several years ago with an emerging force to become one of the largest and a leading diversified business in industrial Conglomerates in Africa.
The Group which is 100% wholly owned indigenous Ghanaian Company focuses on provision of local, value-added products and services that meet the needs of the African population. The Group is headquartered in Accra, Ghana with interests across a range of sectors in Africa.
We are currently into Food & Beverage, Real Estate Development, Transportation, Health Care, Consumer Products Distribution, Agro Processing, Manufacturing, ICT, Exports & Import, and still counting.
In the next 3 years, we shall announce our ambitions to enter Ghana's largest Oil and Gas industry, playing a strategic role in the petroleum sector with strategic alliances, and help build Ghana's biggest and most important Energy sector in the country.
Inspired by billionaires Ned Harlow, Colin Ashdown, and Efemi Okorusa, Tesku Group (Tesku Foundation) is committed to making a name for itself on the philanthropic circuit and has given away privately and still given to the cause to the needy in the society and some specific social causes in Ghana.
The company is managed by a 5 member board and a 2 member advisory experts who are non-board members.
The company has a vision, mission and it is guided by its core values.
We would like to see a designs that is very professional and looks corporate and can attract investors and partners. It must communicate financial safety and growth and must reflect our logo colors.

```html
<!DOCTYPE html>
<html lang="en">
<head>
<meta charset="utf-8">
<title>Tesku Group</title>
<link rel="stylesheet" href="https://fonts.googleapis.com/css2?family=Arimo:wght@400;700&display=swap">
<style>
:root{
  --blue:#0a9be0;
  --blue-dark:#0787c6;
  --nav-top:#6b6b6b;
  --nav-bottom:#3f3f3f;
  --text:#4a4a4a;
  --heading:#3a3a3a;
  --hero-bg:#ececec;
  --footer:#3b3b3b;
  --footer-bottom:#1f1f1f;
  --white:#ffffff;
  --rule:#dedede;
}
*{box-sizing:border-box;margin:0;padding:0}
html,body{width:1200px;height:946px;overflow:hidden}
body{position:relative;background:var(--white);font-family:"Arimo",Arial,sans-serif;color:var(--text)}
a{color:inherit;text-decoration:none}

.site-header{position:absolute;left:0;top:0;width:1200px;height:89px;background:linear-gradient(#f2f2f2 0,#fff 6px)}
.brand{position:absolute;left:243px;top:34px;display:flex;align-items:center;gap:8px;font-size:17px;color:var(--heading)}
.brand-dot{width:22px;height:22px;border-radius:50%;background:var(--blue)}
.follow{position:absolute;left:877px;top:4px;width:96px;height:25px;background:#e2e2e2;display:flex;align-items:center;justify-content:center;gap:5px;font-size:10px;color:#555}
.follow-square{width:16px;height:16px;background:var(--blue-dark)}

.main-nav{position:absolute;left:0;top:89px;width:1200px;height:27px;background:linear-gradient(var(--nav-top),var(--nav-bottom))}
.main-nav a{position:absolute;top:0;height:27px;line-height:27px;font-size:11px;color:var(--white);text-transform:uppercase}
.main-nav a.active{background:var(--blue);padding:0 11px}
.dropdown{position:absolute;left:597px;top:116px;width:144px;background:var(--blue);z-index:3}
.dropdown a{display:block;height:22px;line-height:22px;padding-left:9px;font-size:9.5px;color:var(--white);border-top:1px solid rgba(255,255,255,.25)}

.hero-band{position:absolute;left:0;top:116px;width:1200px;height:270px;background:var(--hero-bg)}
.hero-photo{position:absolute;left:227px;top:123px;width:746px;height:263px;background:linear-gradient(90deg,#dfe8ee 0,#f4f7f9 45%,#e6eef3 100%)}
.hero-caption{position:absolute;left:659px;top:199px;width:314px;height:127px;background:rgba(255,255,255,.9);padding:13px 196px 0 17px;padding-right:22px}
.hero-caption h2{font-weight:400;font-size:20px;color:var(--blue);margin-bottom:8px}
.hero-caption p{font-size:13px;line-height:19px;text-align:justify;color:#555}

.intro-col{position:absolute;top:415px;width:217px}
.intro-col h3{font-weight:400;font-size:18px;color:var(--heading);margin-bottom:10px}
.intro-col p{font-size:10.5px;line-height:13.5px;text-align:justify;height:102px}
.btn{display:inline-block;width:109px;height:31px;line-height:31px;text-align:center;background:var(--blue);color:var(--white);font-size:11px;font-weight:700;margin-left:3px}

.divider{position:absolute;left:225px;top:605px;width:748px;height:1px;background:var(--rule)}
.services-title{position:absolute;left:0;top:625px;width:1200px;text-align:center;font-weight:400;font-size:17px;color:var(--heading)}
.service{position:absolute;width:240px}
.service-icon{position:absolute;left:0;top:6px;width:40px;height:34px;border-radius:4px}
.service-body{position:absolute;left:46px;top:0;width:188px}
.service-body h4{font-size:11.5px;color:var(--blue);margin-bottom:2px}
.service-body p{font-size:10px;line-height:13.5px;text-align:justify}

.site-footer{position:absolute;left:0;top:874px;width:1200px;height:43px;background:var(--footer);text-align:center;line-height:43px;font-size:9.5px;color:var(--white)}
.site-footer span{margin:0 4px}
.copyright{position:absolute;left:0;top:917px;width:1200px;height:29px;background:var(--footer-bottom);text-align:center;line-height:29px;font-size:9.5px;color:#ddd}
</style>
</head>
<body>
<header class="site-header">
  <div class="brand"><span class="brand-dot"></span>TESKU GROUP</div>
  <div class="follow">Follow Us <span class="follow-square"></span><span class="follow-square"></span></div>
</header>

<nav class="main-nav">
  <a href="#" style="left:248px">Home</a>
  <a href="#" style="left:308px">About Us</a>
  <a href="#" style="left:390px">Why Tesku Group</a>
  <a href="#" style="left:517px">Our Vision</a>
  <a href="#" class="active" style="left:597px">Our Services</a>
  <a href="#" style="left:715px">Join Our Team</a>
  <a href="#" style="left:825px">Career</a>
  <a href="#" style="left:898px">Contact</a>
</nav>
<div class="dropdown">
  <a href="#">Food &amp; Beverage</a>
  <a href="#">Real Estate Development</a>
  <a href="#">Transportation</a>
  <a href="#">Health Care</a>
</div>

<section class="hero-band">
</section>
<div class="hero-photo" role="img" aria-label="Photograph of a smiling team of doctors and nurses in white coats"></div>
<div class="hero-caption">
  <h2>Health Care</h2>
  <p>Lorem Ipsum is simply dummy text of the printing and typesetting industry. Lorem Ipsum has been the industry's standard dummy text ever since the 1500s,</p>
</div>

<article class="intro-col" style="left:244px">
  <h3>Who We Are</h3>
  <p>Lorem Ipsum is simply dummy text of the printing and typesetting industry. Lorem Ipsum has been the industry's standard dummy text ever since the 1500s, when an unknown printer took a galley of type and scrambled it to make</p>
  <a href="#" class="btn">Get to Know Us</a>
</article>
<article class="intro-col" style="left:490px">
  <h3>We're Growing!</h3>
  <p>Lorem Ipsum is simply dummy text of the printing and typesetting industry. Lorem Ipsum has been the industry's standard dummy text ever since the 1500s, when an unknown printer took a galley of type and scrambled it to make</p>
  <a href="#" class="btn">Get to Know Us</a>
</article>
<article class="intro-col" style="left:740px">
  <h3>Let's Talk about us</h3>
  <p>Lorem Ipsum is simply dummy text of the printing and typesetting industry. Lorem Ipsum has been the industry's standard dummy text ever since the 1500s, when an unknown printer took a galley of type and scrambled it to make</p>
  <a href="#" class="btn">Get to Know Us</a>
</article>

<div class="divider"></div>
<h2 class="services-title">Our Services</h2>

<div class="service" style="left:232px;top:665px"><div class="service-icon" role="img" aria-label="Icon of a cake slice" style="background:#e8846a"></div><div class="service-body"><h4>Food &amp; Beverage</h4><p>Lorem Ipsum is simply dummy text of the printing and typesetting industry.</p></div></div>
<div class="service" style="left:485px;top:665px"><div class="service-icon" role="img" aria-label="Icon of a house" style="background:#b89a70"></div><div class="service-body"><h4>Real Estate Development</h4><p>Lorem Ipsum is simply dummy text of the printing and typesetting industry.</p></div></div>
<div class="service" style="left:723px;top:665px"><div class="service-icon" role="img" aria-label="Icon of a delivery truck" style="background:#e9a12a"></div><div class="service-body"><h4>Transportation</h4><p>Lorem Ipsum is simply dummy text of the printing and typesetting industry.</p></div></div>

<div class="service" style="left:232px;top:730px"><div class="service-icon" role="img" aria-label="Icon of a medicine bottle" style="background:#c9a04a"></div><div class="service-body"><h4>Health Care</h4><p>Lorem Ipsum is simply dummy text of the printing and typesetting industry.</p></div></div>
<div class="service" style="left:485px;top:730px"><div class="service-icon" role="img" aria-label="Icon of a product document" style="background:#d8d2c4"></div><div class="service-body"><h4>Consumer Products Distribution</h4><p>Lorem Ipsum is simply dummy text of the printing and typesetting industry.</p></div></div>
<div class="service" style="left:723px;top:730px"><div class="service-icon" role="img" aria-label="Icon of gears" style="background:#c3ccd4"></div><div class="service-body"><h4>Agro Processing</h4><p>Lorem Ipsum is simply dummy text of the printing and typesetting industry.</p></div></div>

<div class="service" style="left:232px;top:797px"><div class="service-icon" role="img" aria-label="Icon of colourful gears" style="background:#e9b23a"></div><div class="service-body"><h4>Manufacturing</h4><p>Lorem Ipsum is simply dummy text of the printing and typesetting industry.</p></div></div>
<div class="service" style="left:485px;top:797px"><div class="service-icon" role="img" aria-label="ICT lettering icon" style="background:#3a3a3a"></div><div class="service-body"><h4>ICT</h4><p>Lorem Ipsum is simply dummy text of the printing and typesetting industry.</p></div></div>
<div class="service" style="left:723px;top:797px"><div class="service-icon" role="img" aria-label="Icon of shapes with exchange arrows" style="background:#d9533a"></div><div class="service-body"><h4>Exports &amp; Import</h4><p>Lorem Ipsum is simply dummy text of the printing and typesetting industry.</p></div></div>

<footer class="site-footer">
  <a href="#">Home</a><span>|</span><a href="#">About Us</a><span>|</span><a href="#">why TESKU group</a><span>|</span><a href="#">Our Vision</a><span>|</span><a href="#">Our Services</a><span>|</span><a href="#">join our team</a><span>|</span><a href="#">career</a><span>|</span><a href="#">Contact</a>
</footer>
<div class="copyright">Copyright © 2014 TESKU Group .&nbsp; All Rights Reserved</div>
</body>
</html>
```